Building Referrer Relationships Booklet

4 page A4 booklet to give to potential professional referrers to establish a collaborative relationship.Needs to be bright, vibrant, colourful, friendly, inviting, in keeping with The Wren Clinic colours.
Want to provide potential referrer partners a great reason to choose to collaborate with us. They need to know who we are, what makes us different/appealing, and who we are looking for to connect with.
The final product should communicate high performance and connectedness.

Target Market(s)

professional medical allied health and fitness practitioners

Industry/Entity Type

Health

Requirements
Must have
• energetic, vibrant, engaging, inviting, images

```html
<!DOCTYPE html>
<html lang="en">
<head>
<meta charset="utf-8">
<title>The Wren Clinic – About Us</title>
<link rel="stylesheet" href="https://fonts.googleapis.com/css2?family=Nunito:ital,wght@0,700;0,800;0,900;1,800&family=Open+Sans:wght@400;600&display=swap">
<style>
:root{
  --orange:#f7941d;
  --orange-deep:#f26b1d;
  --amber:#fbb040;
  --ink:#1a1a1a;
  --paper:#ffffff;
  --skin-light:#e9c3a0;
  --skin-dark:#b98262;
}
*{margin:0;padding:0;box-sizing:border-box}
html,body{width:849px;height:1200px;overflow:hidden;background:var(--paper)}
.page{position:relative;width:849px;height:1200px;background:var(--paper);color:var(--ink);font-family:"Open Sans",Arial,sans-serif;overflow:hidden}
.wave{position:absolute;left:0;width:849px}
.wave--top{top:0;height:60px}
.wave--bottom{bottom:0;height:110px}
.heading{font-family:"Nunito",Arial,sans-serif;font-weight:900;color:var(--orange);text-shadow:1px 1px 0 rgba(0,0,0,.15)}
.about-title{position:absolute;left:46px;top:74px;font-size:31px}
.values-title{position:absolute;left:0;width:849px;top:130px;text-align:center;font-size:19px;letter-spacing:.5px;font-style:italic;font-weight:800}
.values{position:absolute;left:46px;top:172px;width:760px;font-size:13.6px;line-height:19px}
.values p{margin-bottom:1px}
.values .key{color:var(--orange);font-weight:600}
.mission{position:absolute;left:60px;width:730px;top:367px;text-align:center;font-size:21.5px;line-height:27px;font-style:italic;font-weight:800}
.love-title{position:absolute;left:0;width:849px;top:452px;text-align:center;font-family:"Nunito",Arial,sans-serif;font-weight:700;font-size:19.5px}
.love-list{position:absolute;left:110px;top:495px;width:560px;list-style:none}
.love-list li{margin-bottom:9px}
.love-list .point{font-family:"Nunito",Arial,sans-serif;font-weight:700;font-size:20px;line-height:25px}
.love-list .detail{font-size:12.5px;line-height:16px}
.foot-photo{position:absolute;left:562px;top:640px;width:178px;height:195px;border-radius:46% 40% 30% 34%;background:radial-gradient(ellipse at 45% 40%,var(--skin-light),var(--skin-dark))}
.team-title{position:absolute;left:46px;top:873px;font-size:25px}
.team-list{position:absolute;left:46px;top:922px;list-style:none;font-family:"Nunito",Arial,sans-serif;font-weight:700;font-size:16.5px;line-height:26px}
</style>
</head>
<body>
<main class="page">
  <svg class="wave wave--top" viewBox="0 0 849 60" preserveAspectRatio="none" aria-hidden="true">
    <defs><linearGradient id="waveTop" x1="0" x2="1"><stop offset="0" stop-color="#fbb040"/><stop offset="1" stop-color="#f26b1d"/></linearGradient></defs>
    <path d="M0 0H849V22C700 48 520 10 360 26C220 40 100 30 0 18Z" fill="url(#waveTop)"/>
    <path d="M0 18C100 30 220 40 360 26C520 10 700 48 849 22V30C700 56 520 20 360 36C220 48 100 38 0 26Z" fill="#fbb040" opacity=".6"/>
  </svg>

  <h1 class="heading about-title">About Us:</h1>
  <h2 class="heading values-title">COURAGE INSPIRATION&nbsp; FUN CREATIVE WOW TEAM</h2>

  <section class="values">
    <p><span class="key">Courage</span> gives us the strength and confidence to take risks and embrace challenges</p>
    <p><span class="key">Inspiration</span> is our energy, our fuel for success, that life force that feeds us as we grow and develop.</p>
    <p><span class="key">Fun</span> generates happiness, and we all function at our best when we are happy.</p>
    <p><span class="key">Creativity</span> sets us as an innovative leading-edge business.</p>
    <p><span class="key">Wow</span> means being the very best we can be and realise our true potential.We are not your average business, our service is not average, and our people are not average.</p>
    <p><span class="key">Team</span> and in particular high-performanceteam means we perform at our very best. Great teamwork creates unity and we accomplish much more than each of us alone.</p>
  </section>

  <h2 class="heading mission">At The Wren Clinic we are passionate about building strong postural foundations, from the feet up.</h2>

  <h3 class="love-title">The top 3 things our clients love about us (and hopefully yours will too!):</h3>
  <ol class="love-list">
    <li><div class="point">1. Positive energy, enthusiasm and outcomes</div><div class="detail">NPS average score &gt;9 out of 10</div></li>
    <li><div class="point">2. Trusted leader in the practice of podiatric medicine</div><div class="detail">established 1999, elite experience, latest high-tech equipment</div></li>
    <li><div class="point">3. Focus is on strong feet, not just orthotics!</div><div class="detail">Stridewell Barefoot Method, Fascial Lines, Hands-On Foot Therapies</div></li>
  </ol>

  <div class="foot-photo" role="img" aria-label="Photo of a bare foot sole"></div>

  <h2 class="heading team-title">Our Team:</h2>
  <ul class="team-list">
    <li>Dr Marcus Ellery (Principal Podiatrist)</li>
    <li>Dr Hannah Colby (Senior Podiatrist)</li>
    <li>Dr Isla Penrose (Podiatrist)</li>
    <li>Dr Julian Tarrow (Podiatrist)</li>
    <li>Nadia Fenwick (Practice Manager)</li>
    <li>Tessa Marlow (Front Office Administrator)</li>
  </ul>

  <svg class="wave wave--bottom" viewBox="0 0 849 110" preserveAspectRatio="none" aria-hidden="true">
    <defs><linearGradient id="waveBottom" x1="0" x2="1"><stop offset="0" stop-color="#f26b1d"/><stop offset=".6" stop-color="#f7941d"/><stop offset="1" stop-color="#fbb040"/></linearGradient></defs>
    <path d="M0 40C160 10 330 70 500 50C650 32 760 20 849 36V110H0Z" fill="#fbb040" opacity=".55"/>
    <path d="M0 60C170 30 340 88 510 68C660 50 770 42 849 56V110H0Z" fill="url(#waveBottom)"/>
  </svg>
</main>
</body>
</html>
```